Maplecrest Apartments Downtown Northport

We are looking to redesign our entry way sign at Maplecrest Apartments, a low density residential apartment building, located in Downtown Northport, Alabama, U.S. Downtown Northport is a bustling boutique business district with a small town feel comprised of shops, restaurants, and a renowned arts community known for Varrow Arts Center and Festival which is one of the nation's top outdoor arts festivals. Maplecrest Apartments and its sign is the first thing you seen when you enter Downtown Northport. We are looking to redesign our sign, entry way and landscaping to compliment the building and character of the historic downtown.

Target Market(s)

Our apartment building is comprised of 20 apartments units with tenants who are primarily part of the local workforce, young professionals, or students at the Halverton College or other nearby institutions.

Requirements
Must have
• The name of the apartment building - Maplecrest
Phone number on the sign 205-555-0148

```html
<!DOCTYPE html>
<html lang="en">
<head>
<meta charset="utf-8">
<title>Maplecrest Entry Sign</title>
<link rel="stylesheet" href="https://fonts.googleapis.com/css2?family=Kurale&family=Poppins:wght@800&display=swap">
<style>
  :root {
    --page-bg: #adadad;
    --sign-white: #ffffff;
    --ray-grey: #e6e6e6;
    --orange-light: #f29a1e;
    --orange-deep: #ea650a;
    --band-orange: #ef7d06;
    --swoosh-pale: #f4a04d;
    --swoosh-mid: #ea843e;
    --swoosh-dark: #df620b;
    --shadow-grey: #c4c4c4;
    --phone-white: #ffffff;
  }
  html, body {
    margin: 0;
    padding: 0;
    width: 1200px;
    height: 1200px;
    overflow: hidden;
    background: var(--page-bg);
  }
  .canvas {
    position: relative;
    width: 1200px;
    height: 1200px;
    display: flex;
    align-items: center;
    justify-content: center;
  }
  .sign {
    position: relative;
    width: 1100px;
    height: 400px;
    background: var(--sign-white);
    overflow: hidden;
  }
  .sign__rays,
  .sign__band {
    position: absolute;
    inset: 0;
    width: 1100px;
    height: 400px;
  }
  .sign__name {
    position: absolute;
    left: 0;
    right: 0;
    top: 0;
    margin: 0;
    text-align: center;
    font-family: "Kurale", serif;
    font-weight: 400;
    font-size: 200px;
    line-height: 1;
    padding-top: 34px;
    letter-spacing: -2px;
    background: linear-gradient(180deg, var(--orange-light) 25%, var(--orange-deep) 80%);
    -webkit-background-clip: text;
    background-clip: text;
    color: transparent;
    filter: drop-shadow(5px 5px 0 var(--shadow-grey));
  }
  .sign__contact {
    position: absolute;
    left: 230px;
    top: 318px;
    display: flex;
    align-items: center;
    gap: 20px;
    color: var(--phone-white);
    font-family: "Poppins", sans-serif;
    font-weight: 800;
    font-size: 62px;
    line-height: 1;
    letter-spacing: 0.5px;
  }
  .sign__phone-icon {
    width: 50px;
    height: 50px;
    flex: none;
  }
</style>
</head>
<body>
  <main class="canvas">
    <section class="sign" aria-label="Maplecrest Apartments entry sign">
      <svg class="sign__rays" viewBox="0 0 1100 400" aria-hidden="true">
        <defs>
          <radialGradient id="rayFade" cx="550" cy="330" r="650" gradientUnits="userSpaceOnUse">
            <stop offset="0.25" stop-color="#ffffff" stop-opacity="0"/>
            <stop offset="1" stop-color="#dcdcdc" stop-opacity="1"/>
          </radialGradient>
        </defs>
        <g fill="url(#rayFade)">
          <polygon points="550,330 0,0 0,70"/>
          <polygon points="550,330 0,150 0,210"/>
          <polygon points="550,330 0,270 0,320"/>
          <polygon points="550,330 120,0 200,0"/>
          <polygon points="550,330 320,0 390,0"/>
          <polygon points="550,330 500,0 560,0"/>
          <polygon points="550,330 690,0 760,0"/>
          <polygon points="550,330 880,0 960,0"/>
          <polygon points="550,330 1100,20 1100,90"/>
          <polygon points="550,330 1100,160 1100,220"/>
          <polygon points="550,330 1100,270 1100,320"/>
        </g>
      </svg>

      <svg class="sign__band" viewBox="0 0 1100 400" aria-hidden="true">
        <path fill="var(--swoosh-dark)" d="M0,318 L820,306 C1000,302 1085,318 1100,400 L0,400 Z"/>
        <path fill="var(--swoosh-mid)" d="M0,318 L820,306 C975,302 1055,316 1072,400 L0,400 Z"/>
        <path fill="var(--swoosh-pale)" d="M0,318 L820,306 C950,302 1030,314 1046,400 L0,400 Z"/>
        <path fill="var(--band-orange)" d="M0,318 L820,306 C920,302 1002,312 1016,400 L0,400 Z"/>
      </svg>

      <h1 class="sign__name">Maplecrest</h1>

      <p class="sign__contact" style="margin:0;">
        <svg class="sign__phone-icon" viewBox="0 0 50 50" aria-hidden="true">
          <circle cx="25" cy="25" r="25" fill="var(--phone-white)"/>
          <path fill="var(--band-orange)" d="M17 13c1.2-.8 2.4-.6 3.1.5l2.6 4c.6 1 .4 2.1-.5 2.8l-1.6 1.2c.9 2.4 2.6 4.6 5 6.3l1.4-1.4c.8-.8 2-.9 2.9-.2l3.8 2.9c1 .8 1.1 2 .3 3.1l-1.6 2c-1.2 1.4-3.1 1.8-4.9 1.1C19.6 33 14.7 27.6 13 20.8c-.5-2 .2-4 1.8-5.3z"/>
          <path fill="none" stroke="var(--band-orange)" stroke-width="2" stroke-linecap="round" d="M27 15a9 9 0 0 1 8 8M27 11a13 13 0 0 1 12 12"/>
        </svg>
        <span class="sign__phone-number">205-555-0148</span>
      </p>
    </section>
  </main>
</body>
</html>
```